Design a web site for my business - Brellan Coatworks Mackaby.

We are a family business that handles design, fabrication and installation of powder coated aluminum, stainless steel and glass products. Including handrails, privacy slat screens, electric gates and pool fencing. We are based in the Whitsundays in North Queensland and service an area from Airlie Beach to Townsville.

Target Market(s)

Domestic and commercial

Industry/Entity Type

fabrication - manufacturing

Coding

Coded - Design and coding required

Number of Pages Required

5+ page

Colors
0054AA
0677BA
7BADD7
CADEEF
E8F1F8

Requirements
Must have
• photo galleries, contact page, one page for privacy screens, balustrades, glass fencing, stainless steel handrail, powder coated aluminium handrails and pool fencing

```html
<!DOCTYPE html>
<html lang="en">
<head>
<meta charset="utf-8">
<title>Contact – Brellan Coatworks Mackaby</title>
<link href="https://fonts.googleapis.com/css2?family=Inter:wght@400;500;600&family=Montserrat:wght@600;700&display=swap" rel="stylesheet">
<style>
:root{
  --ink:#1a1f22;
  --ink-soft:#3a4248;
  --muted:#66717a;
  --blue:#0054AA;
  --blue-mid:#0677BA;
  --blue-light:#7BADD7;
  --blue-pale:#CADEEF;
  --page:#f4f9fd;
  --field:#eef4f8;
  --line:#c7d3dc;
  --white:#ffffff;
}
*{box-sizing:border-box;margin:0;padding:0}
html,body{width:813px;height:1200px;overflow:hidden}
body{position:relative;background:var(--page);font-family:"Inter",sans-serif;color:var(--ink)}
.site-header{position:absolute;left:0;top:0;width:813px;height:51px;border-bottom:1px solid #e3eaef;background:var(--page)}
.brand{position:absolute;left:42px;top:17px;font-family:"Montserrat",sans-serif;font-weight:600;font-size:15px;letter-spacing:-.4px;color:var(--ink)}
.main-nav{position:absolute;left:437px;top:19px;display:flex;gap:20px;font-size:9px;font-weight:500;letter-spacing:.3px;color:var(--ink-soft)}
.main-nav .active{color:var(--blue-mid);font-weight:600;border-bottom:1px solid var(--blue-mid);padding-bottom:2px;margin-top:-2px}
.quote-btn{position:absolute;left:667px;top:15px;width:103px;height:22px;background:var(--ink);color:var(--white);border-radius:3px;font-size:8.5px;font-weight:600;display:flex;align-items:center;justify-content:center;letter-spacing:.2px}
.intro{position:absolute;left:42px;top:81px;width:420px}
.eyebrow{font-size:9px;font-weight:600;letter-spacing:1.4px;color:var(--blue-mid)}
.intro h1{margin-top:13px;font-family:"Montserrat",sans-serif;font-weight:700;font-size:31px;line-height:37px;letter-spacing:-.3px;color:var(--ink)}
.intro p{margin-top:13px;width:360px;font-size:11.4px;line-height:18.4px;color:var(--ink-soft)}
.card{position:absolute;background:var(--white);border:1px solid #e2e9ef;border-radius:7px}
.quote-form{left:42px;top:287px;width:419px;height:449px;padding:31px 30px}
.grid{display:grid;grid-template-columns:171px 171px;column-gap:15px;row-gap:0}
.field{margin-bottom:18px}
.field label{display:block;font-size:8.8px;font-weight:500;letter-spacing:.3px;color:var(--ink);margin-bottom:7px}
.input{height:31px;background:var(--field);border:1px solid var(--line);border-radius:3px;padding:0 8px;display:flex;align-items:center;font-size:10px;color:#7b868e}
.input.filled{color:var(--ink)}
.input.select{justify-content:space-between}
.field.wide{grid-column:1 / 3}
.textarea{height:92px;align-items:flex-start;padding-top:8px;line-height:15px}
.submit{margin-top:6px;height:36px;border-radius:3px;background:linear-gradient(90deg,#2c3237,var(--ink));color:var(--white);font-size:9.5px;font-weight:600;letter-spacing:.3px;display:flex;align-items:center;justify-content:center;gap:8px;box-shadow:0 6px 12px rgba(26,31,34,.18)}
.contact-info{left:477px;top:287px;width:295px;height:239px;padding:20px 20px}
.contact-row{display:flex;gap:10px;align-items:flex-start;margin-bottom:16px}
.icon-dot{width:30px;height:30px;border-radius:50%;background:#e6eef5;display:flex;align-items:center;justify-content:center;flex:none;margin-top:0}
.contact-row small{display:block;font-size:8.8px;font-weight:500;letter-spacing:.3px;color:var(--ink)}
.phone{font-family:"Montserrat",sans-serif;font-weight:600;font-size:15px;color:var(--ink);margin-top:1px}
.email{font-size:11.4px;color:var(--ink);margin-top:2px}
.hours{border-top:1px solid var(--line);margin-top:-2px;padding-top:13px}
.hours h2{font-size:8.8px;font-weight:500;letter-spacing:.6px;color:var(--ink);margin-bottom:10px}
.hours-row{display:flex;justify-content:space-between;font-size:10px;color:var(--ink-soft);height:26.5px}
.hours-row b{font-weight:600;color:var(--ink)}
.service-map{position:absolute;left:477px;top:541px;width:295px;height:253px;border-radius:7px;overflow:hidden;background:linear-gradient(180deg,#c7c7c7 0%,#c9c9c9 70%,#d6d6d6 100%)}
.region-card{position:absolute;left:11px;top:177px;width:273px;height:66px;background:rgba(255,255,255,.93);border-radius:4px;padding:9px 11px}
.region-card h3{font-size:9.5px;font-weight:600;color:var(--blue-mid);letter-spacing:.2px}
.region-card p{margin-top:4px;font-size:10px;line-height:16px;color:var(--ink-soft)}
.local-badge{position:absolute;left:477px;top:810px;width:295px;height:81px;border-radius:7px;background:radial-gradient(circle at 88% 60%,#1b3550 0%,#1a2127 45%,var(--ink) 100%);padding:22px 15px}
.local-badge h3{font-family:"Montserrat",sans-serif;font-weight:600;font-size:15.5px;color:var(--white)}
.local-badge p{margin-top:3px;font-size:10px;color:#c9d0d5}
.badge-ring{position:absolute;left:229px;top:15px;width:51px;height:51px;border-radius:50%;border:2px solid var(--blue);background:#16324d;display:flex;align-items:center;justify-content:center}
.site-footer{position:absolute;left:0;top:943px;width:813px;height:257px;background:var(--ink);border-top:1px solid #2a3136}
.footer-brand{position:absolute;left:42px;top:52px;width:170px}
.footer-brand .name{font-family:"Montserrat",sans-serif;font-weight:700;font-size:13px;line-height:19px;color:#232b30}
.footer-brand p{margin-top:18px;font-size:10px;line-height:16.2px;color:#8d969c}
.footer-col{position:absolute;top:52px}
.footer-col h4{font-size:8.8px;font-weight:600;letter-spacing:1.2px;color:var(--white);margin-bottom:10px}
.footer-col li{list-style:none;font-size:7.6px;color:#8d969c;height:14px}
.footer-bottom{position:absolute;left:0;top:208px;width:813px;border-top:1px solid #262d32;padding:21px 42px 0;font-size:7.6px;color:#8d969c}
</style>
</head>
<body>
<header class="site-header">
  <div class="brand">BRELLAN COATWORKS</div>
  <nav class="main-nav"><span>Home</span><span>Products</span><span>Process</span><span class="active">Projects</span></nav>
  <div class="quote-btn">Request a Quote</div>
</header>

<section class="intro">
  <div class="eyebrow">GET IN TOUCH</div>
  <h1>Precision Engineering for Coastal Excellence</h1>
  <p>Whether you're planning a luxury pool fence or a custom electric gate, our team is ready to bring structural integrity and aesthetic clarity to your project.</p>
</section>

<form class="card quote-form">
  <div class="grid">
    <div class="field"><label>First Name</label><div class="input">John</div></div>
    <div class="field"><label>Last Name</label><div class="input">Doe</div></div>
    <div class="field"><label>Email Address</label><div class="input">john@example.com</div></div>
    <div class="field"><label>Phone Number</label><div class="input">0400 000 000</div></div>
    <div class="field"><label>Project Type</label><div class="input filled select">Glass Pool Fencing
      <svg width="9" height="6" viewBox="0 0 9 6"><path d="M1 1l3.5 3.5L8 1" fill="none" stroke="#3a4248" stroke-width="1.2"/></svg></div></div>
    <div class="field"><label>Project Location</label><div class="input">e.g. Airlie Beach</div></div>
    <div class="field wide"><label>Project Details</label><div class="input textarea">Tell us about your requirements, measurements, or any specific design ideas you have...</div></div>
  </div>
  <div class="submit">
    <svg width="13" height="11" viewBox="0 0 13 11"><path d="M1 1l11 4.5L1 10l2-4.5z M3 5.5h9" fill="none" stroke="#fff" stroke-width="1.1" stroke-linejoin="round"/></svg>
    Submit Quote Request
  </div>
</form>

<aside class="card contact-info">
  <div class="contact-row">
    <div class="icon-dot"><svg width="12" height="12" viewBox="0 0 24 24"><path d="M5 3h4l2 5-2.5 1.5a11 11 0 0 0 6 6L16 13l5 2v4a2 2 0 0 1-2 2A16 16 0 0 1 3 5a2 2 0 0 1 2-2z" fill="none" stroke="#0054AA" stroke-width="2"/></svg></div>
    <div><small>Call Us Directly</small><div class="phone">0400 555 019</div></div>
  </div>
  <div class="contact-row">
    <div class="icon-dot"><svg width="12" height="10" viewBox="0 0 24 18"><rect x="1" y="1" width="22" height="16" rx="2" fill="none" stroke="#0054AA" stroke-width="2"/><path d="M1 3l11 7 11-7" fill="none" stroke="#0054AA" stroke-width="2"/></svg></div>
    <div><small>Email Enquiries</small><div class="email">info@brellancoatworks.com.au</div></div>
  </div>
  <div class="hours">
    <h2>BUSINESS HOURS</h2>
    <div class="hours-row"><span>Monday - Friday</span><b>7:00 AM - 4:30 PM</b></div>
    <div class="hours-row"><span>Saturday</span><b>By Appointment</b></div>
    <div class="hours-row"><span>Sunday</span><b>Closed</b></div>
  </div>
</aside>

<div class="service-map" role="img" aria-label="Greyscale map of the Whitsunday coast and islands showing the service region">
  <div class="region-card">
    <h3>Service Region</h3>
    <p>Servicing all areas from Airlie Beach to Townsville, including Bowen and the Burdekin region.</p>
  </div>
</div>

<div class="local-badge">
  <h3>Locally Crafted</h3>
  <p>Whitsunday Owned &amp; Family Operated.</p>
  <div class="badge-ring"><svg width="16" height="20" viewBox="0 0 16 20"><circle cx="8" cy="7" r="5.5" fill="none" stroke="#0054AA" stroke-width="1.6"/><path d="M4.5 11.5V18l3.5-2 3.5 2v-6.5" fill="none" stroke="#0054AA" stroke-width="1.6"/></svg></div>
</div>

<footer class="site-footer">
  <div class="footer-brand">
    <div class="name">Brellan Coatworks Mackaby</div>
    <p>Specializing in high-end metal and glass fabrication for premium coastal properties.</p>
  </div>
  <div class="footer-col" style="left:228px"><h4>SOLUTIONS</h4><ul><li>Handrails</li><li>Slat Screens</li><li>Electric Gates</li><li>Pool Fencing</li></ul></div>
  <div class="footer-col" style="left:415px"><h4>LOCATIONS</h4><ul><li>Airlie Beach</li><li>Townsville</li><li>Bowen</li></ul></div>
  <div class="footer-col" style="left:601px"><h4>LEGAL</h4><ul><li>Privacy Policy</li><li>Terms of Service</li></ul></div>
  <div class="footer-bottom">© 2024 Brellan Coatworks Mackaby. All Rights Reserved. Australian Made.</div>
</footer>
</body>
</html>
```